Stationery Design Project

See the detainl of the Basic company project I also have live: http://briefs.marlowgrid.net/brief.aspx?id=306182

Reason: I am waiting to select a logo design and ideally the stationery will be from the same person

Industry/Entity Type

It Company

```html
<!DOCTYPE html>
<html lang="en">
<head>
<meta charset="utf-8">
<title>Veloria LLP Letterhead</title>
<link rel="stylesheet" href="https://fonts.googleapis.com/css2?family=Quicksand:wght@600;700&display=swap">
<style>
  :root {
    --ink-navy: #232d7c;
    --leaf-blue: #1fa3e0;
    --paper: #ffffff;
    --frame: #2a2a2a;
  }
  html, body {
    margin: 0;
    padding: 0;
    overflow: hidden;
    background: var(--paper);
  }
  .letterhead {
    position: relative;
    width: 860px;
    height: 1200px;
    box-sizing: border-box;
    border: 1px solid var(--frame);
    background: var(--paper);
    font-family: "Quicksand", sans-serif;
    color: var(--ink-navy);
    overflow: hidden;
  }
  .brand {
    position: absolute;
    left: 98px;
    top: 132px;
    display: flex;
    align-items: center;
    gap: 12px;
  }
  .brand-dot {
    width: 30px;
    height: 30px;
    border-radius: 50%;
    background: var(--leaf-blue);
  }
  .brand-name {
    font-size: 30px;
    font-weight: 700;
    letter-spacing: 0.3px;
    color: var(--ink-navy);
  }
  .office-details {
    position: absolute;
    right: 94px;
    top: 117px;
    text-align: right;
    font-size: 11px;
    font-weight: 700;
    line-height: 13.6px;
    letter-spacing: 0.6px;
  }
  .office-details p {
    margin: 0;
  }
  .partnership-number {
    position: absolute;
    right: 94px;
    top: 189px;
    margin: 0;
    font-size: 11px;
    font-weight: 700;
    letter-spacing: 0.6px;
  }
</style>
</head>
<body>
  <div class="letterhead">
    <div class="brand">
      <span class="brand-dot"></span>
      <span class="brand-name">Veloria LLP</span>
    </div>

    <address class="office-details" style="font-style: normal;">
      <p>Registered Office:</p>
      <p>Alder Court,</p>
      <p>12B Harlow Rd,</p>
      <p>Ashbridge</p>
      <p>AB4 2KL</p>
    </address>

    <p class="partnership-number">Partnership No. OC402715</p>
  </div>
</body>
</html>
```